Banner ad for Gen Y demographic - Training Institute

We are a training organization that requires two (2) banner ads which we can use to promote our brand, our Diploma of Management and Diploma of Business product offerings, you may visit our website: www.pembertonlearninghub.com.au to grab some background information on us.

I have also included our logo to be used in the banner ad (white or black depending on background color). The text to be used throughout the banner ad is Times New Roman please.

We require flash banners that just have the text changing from one slide to the next. We want something clean and enticing. We also need a call to action button “Start now” or something similar.

I have included the below just as a guide but welcome any creativity that you believe would fit our market. I encourage you to be creative!

Flash panels:
1 Slide – I don’t take classes. I experience them – are you in?
2 Slide - Unlock your potential excellence today

I need two different banner ads / sizes please:

1. 600px (W) x 120px (H), max file size 150KB, gif, jpeg, swf
2. 300px(w) x 250px(h), max size 150KB, gif, jpeg, swf

Out target audience is Gen Y, they are looking for ways to improve their careers, make more money, or to get a different job at their existing employer. They’re looking for a Diploma in Management or Business that will give them the education and the piece of paper that will allow them to get that job.

I look forward to seeing what you come up with!

Industry/Entity Type

Training

```html
<!DOCTYPE html>
<html lang="en">
<head>
<meta charset="utf-8">
<title>Training Institute Banner Ads</title>
<link rel="stylesheet" href="https://fonts.googleapis.com/css2?family=Tinos:ital,wght@0,400;0,700;1,400;1,700&display=swap">
<style>
  :root {
    --board: #2c2c2d;
    --board-edge: #1a1a1b;
    --ink: #0b0b12;
    --white: #ffffff;
    --sky-light: #f6f9fc;
    --sky-mid: #dbe7f3;
    --sky-deep: #a9c6e4;
    --hair: #6b4332;
    --skin: #ecc8b0;
    --skin-shadow: #c89a80;
    --blouse: #f1efee;
    --glow-centre: #fbf7ee;
    --glow-mid: #9c8a6c;
    --glow-dark: #0e0a06;
    --teal-light: #8fcdd2;
    --teal: #4e9ea6;
    --teal-deep: #2c6870;
    --figure: #1d2a30;
    --button-top: #4a4a4a;
    --button-bottom: #0c0c0c;
  }
  * { margin: 0; padding: 0; box-sizing: border-box; }
  html, body { width: 1200px; height: 942px; overflow: hidden; }
  body {
    background: radial-gradient(ellipse at 50% 40%, var(--board) 0%, var(--board-edge) 100%);
    font-family: "Tinos", "Times New Roman", serif;
    position: relative;
  }
  .banner {
    position: absolute;
    overflow: hidden;
    box-shadow: 0 3px 10px rgba(0,0,0,.55);
  }
  .banner--wide { width: 805px; height: 161px; }
  .banner--square { width: 403px; height: 335px; }
  .banner--puzzle { left: 126px; top: 123px; }
  .banner--glasses { left: 129px; top: 323px; }
  .banner--key-light { left: 122px; top: 533px; }
  .banner--key-figure { left: 552px; top: 533px; }

  .photo { position: absolute; }
  .photo--puzzle-sky {
    inset: 0;
    background:
      radial-gradient(ellipse 220px 120px at 80px 60px, rgba(169,198,228,.55) 0%, rgba(169,198,228,0) 100%),
      radial-gradient(ellipse 260px 110px at 560px 140px, rgba(169,198,228,.45) 0%, rgba(169,198,228,0) 100%),
      linear-gradient(90deg, var(--sky-mid) 0%, var(--sky-light) 40%, var(--sky-light) 100%);
  }
  .photo--smiling-student {
    right: 0; top: 0; width: 133px; height: 161px;
    background:
      radial-gradient(ellipse 48px 58px at 70px 58px, var(--skin) 0%, var(--skin) 55%, rgba(236,200,176,0) 100%),
      linear-gradient(180deg, var(--hair) 0%, #8a5a44 45%, var(--blouse) 78%, var(--blouse) 100%);
  }
  .photo--glasses-sky {
    inset: 0;
    background:
      radial-gradient(ellipse 300px 200px at 610px 90px, var(--skin) 0%, var(--skin) 45%, rgba(236,200,176,0) 100%),
      linear-gradient(90deg, var(--sky-light) 0%, #eef3f8 48%, #e9d6c8 56%, var(--skin) 72%, var(--skin-shadow) 100%);
  }
  .photo--glowing-key {
    inset: 0;
    background: radial-gradient(ellipse 260px 240px at 150px 95px, var(--glow-centre) 0%, #ddd2bc 25%, var(--glow-mid) 55%, var(--glow-dark) 100%);
  }
  .photo--teal-backdrop {
    inset: 0;
    background: radial-gradient(circle at 50% 55%, var(--teal-light) 0%, var(--teal) 50%, var(--teal-deep) 100%);
  }
  .photo--key-figure {
    inset: 0;
    background: radial-gradient(ellipse 110px 190px at 110px 170px, rgba(29,42,48,.55) 0%, rgba(29,42,48,.3) 55%, rgba(29,42,48,0) 100%);
  }

  .headline {
    position: absolute;
    font-weight: 700;
    font-style: italic;
    color: var(--ink);
    white-space: nowrap;
    line-height: 1;
  }
  .headline--glow { text-shadow: 0 0 4px var(--white), 0 0 8px var(--white); }
  .banner--puzzle .headline--small { left: 0; width: 684px; text-align: center; top: 12px; font-size: 29px; }
  .banner--puzzle .headline--large { left: 0; width: 690px; text-align: center; top: 48px; font-size: 40px; }
  .banner--glasses .headline { left: 38px; font-size: 29px; }
  .banner--glasses .headline--one { top: 20px; }
  .banner--glasses .headline--two { top: 54px; }

  .unlock {
    position: absolute;
    font-style: italic;
    font-weight: 700;
    line-height: 1;
    white-space: nowrap;
    color: var(--ink);
  }
  .unlock__big {
    font-size: 56px;
    color: var(--white);
    -webkit-text-stroke: 1.5px var(--ink);
    text-shadow: 2px 2px 3px rgba(0,0,0,.6);
  }
  .unlock__your { font-size: 22px; }
  .unlock__line { font-size: 23px; }
  .unlock__today { font-size: 68px; }
  .banner--key-light .unlock--lead { left: 24px; top: 80px; }
  .banner--key-light .unlock--sub { left: 21px; top: 134px; }
  .banner--key-light .unlock--today { left: 230px; top: 112px; }
  .banner--key-light .unlock__line, .banner--key-light .unlock__your { text-shadow: 0 0 4px var(--white); }
  .banner--key-figure .unlock--lead { left: 149px; top: 16px; }
  .banner--key-figure .unlock--sub { left: 166px; top: 74px; }
  .banner--key-figure .unlock--today { left: 230px; top: 112px; }

  .cta {
    position: absolute;
    width: 172px; height: 45px;
    border: 2px solid var(--white);
    border-radius: 4px;
    background: linear-gradient(180deg, var(--button-top) 0%, var(--button-bottom) 100%);
    color: var(--white);
    font-size: 24px;
    font-family: "Tinos", "Times New Roman", serif;
    display: flex; align-items: center; justify-content: center;
    box-shadow: 0 2px 4px rgba(0,0,0,.5);
  }
  .banner--puzzle .cta { left: 255px; top: 103px; }
  .banner--glasses .cta { left: 280px; top: 101px; }
  .banner--key-light .cta { left: 117px; top: 231px; }
  .banner--key-figure .cta { left: 192px; top: 229px; }
</style>
</head>
<body>
  <section class="banner banner--wide banner--puzzle">
    <div class="photo photo--puzzle-sky" role="img" aria-label="Light blue sky with white puzzle pieces"></div>
    <div class="photo photo--smiling-student" role="img" aria-label="Smiling young woman pointing at the message"></div>
    <p class="headline headline--glow headline--small">I don’t take classes.</p>
    <p class="headline headline--glow headline--large">I experience them – Are you in?</p>
    <div class="cta">Start Now</div>
  </section>

  <section class="banner banner--wide banner--glasses">
    <div class="photo photo--glasses-sky" role="img" aria-label="Puzzle pieces fading into a close-up of a young woman wearing glasses"></div>
    <p class="headline headline--glow headline--one">I don’t take classes.</p>
    <p class="headline headline--glow headline--two">I experience them – Are you in?</p>
    <div class="cta">Start Now</div>
  </section>

  <section class="banner banner--square banner--key-light">
    <div class="photo photo--glowing-key" role="img" aria-label="Hand holding an old key in bright rays of light"></div>
    <p class="unlock unlock--lead"><span class="unlock__big">Unlock</span> <span class="unlock__your">your</span></p>
    <p class="unlock unlock--sub"><span class="unlock__line">potential excellence</span></p>
    <p class="unlock unlock--today"><span class="unlock__today">today</span></p>
    <div class="cta">Start Now</div>
  </section>

  <section class="banner banner--square banner--key-figure">
    <div class="photo photo--teal-backdrop"></div>
    <div class="photo photo--key-figure" role="img" aria-label="Illustrated businessman holding a large key labelled success"></div>
    <p class="unlock unlock--lead"><span class="unlock__big">Unlock</span> <span class="unlock__your">your</span></p>
    <p class="unlock unlock--sub"><span class="unlock__line">potential excellence</span></p>
    <p class="unlock unlock--today"><span class="unlock__today">today</span></p>
    <div class="cta">Start Now</div>
  </section>
</body>
</html>
```